Youth Sports Programs needs a catchy and fun facebook page

We need a facebook design for a new Youth Sports Program named PebblePeak Sprinters. The target age group is 2-14 years of age and all Skill level. Sports programs/Clinics offered are Baseball/T-Ball, Flag Football, Basketball,Volleyball and Soccer. Our goal is to provide options to parents with non-school age children as well as keeping the school aged children physically active. In addition, we offer Private/Semi-private lessons and Birthday Party pacakages by special request. Locations are rotating sessions in area parks of The San Fernando Valley.

Target Market(s)

Parents with children 2-14 yrs old

Industry/Entity Type

School

Requirements
Must have
• Capability to upload photos, an area to blog, Catchy phrases that elaborate on fun, skill development, etc.
Nice to have
• Logo that progresses from little to big, as though the athlete began young and grew larger/taller to show diversity and skill development. Really boast a feeling for parents to want to sign up. Would like to have the capability of a registration link

Logo attached is a work in progress, but it gives you a basis to go off of.

```html
<!DOCTYPE html>
<html lang="en">
<head>
<meta charset="utf-8">
<title>PebblePeak Sprinters – Cover</title>
<link href="https://fonts.googleapis.com/css2?family=Open+Sans:ital,wght@0,400;0,600;0,700;1,400&family=Patrick+Hand&display=swap" rel="stylesheet">
<style>
  :root {
    --cover-blue: #4d6fb6;
    --splash: #6f8cc8;
    --navy: #2e4676;
    --profile-navy: #324d82;
    --white: #ffffff;
    --card-white: #fbfbf8;
    --caption: #333333;
    --btn-bg: #f6f7f9;
    --btn-border: #a5a9b2;
    --btn-text: #333333;
    --page: #ffffff;
    --baseball: #8b6a48;
    --tball: #8aa27a;
    --flag: #707070;
    --volley: #d89a2c;
    --soccer: #3f8f3a;
    --hoops: #2b5fae;
  }
  html, body {
    margin: 0;
    width: 1200px;
    height: 564px;
    overflow: hidden;
    background: var(--page);
    font-family: "Open Sans", Arial, sans-serif;
  }
  .page { position: relative; width: 1200px; height: 564px; }

  .cover {
    position: absolute; left: 0; top: 0;
    width: 1200px; height: 444px;
    background: var(--cover-blue);
    overflow: hidden;
  }
  .splash {
    position: absolute; left: 440px; top: 20px;
    width: 440px; height: 400px;
    border-radius: 50%;
    background: radial-gradient(ellipse at center, var(--splash) 0%, var(--splash) 45%, rgba(111,140,200,0) 72%);
  }

  .intro { position: absolute; left: 34px; top: 38px; color: var(--white); }
  .intro__headline {
    margin: 0; font-weight: 400; font-size: 31px; line-height: 39px;
  }
  .intro__ages {
    margin: 18px 0 0; font-style: italic; font-size: 23px; line-height: 30px;
  }
  .intro__signup {
    display: inline-block; margin-top: 14px;
    width: 131px; height: 42px; line-height: 42px;
    text-align: center; border-radius: 6px;
    background: var(--navy); color: var(--white);
    font-weight: 700; font-size: 20px; text-decoration: none;
  }

  .pointers { position: absolute; left: 0; top: 0; width: 1200px; height: 444px; }
  .pointers__label { font-family: "Open Sans", Arial, sans-serif; font-weight: 700; font-size: 13px; fill: var(--white); }
  .pointers__arrow { fill: none; stroke: var(--white); stroke-width: 1.6; stroke-linecap: round; opacity: .85; }

  .snapshot {
    position: absolute;
    margin: 0;
    background: var(--card-white);
    padding: 7px 7px 0;
    box-shadow: 0 3px 8px rgba(0,0,0,.35);
    box-sizing: border-box;
  }
  .snapshot__photo { width: 100%; display: block; }
  .snapshot__caption {
    font-family: "Patrick Hand", cursive;
    font-size: 15px; color: var(--caption);
    text-align: center; line-height: 22px;
    white-space: nowrap;
  }

  /* lower row sits behind the upper row */
  .snapshot--volley { z-index: 1; left: 474px; top: 240px; width: 146px; height: 146px; transform: rotate(-5deg); }
  .snapshot--volley .snapshot__photo { height: 117px; background: linear-gradient(#e7b543, var(--volley) 60%, #6b4a1c); }
  .snapshot--hoops { z-index: 1; left: 728px; top: 212px; width: 140px; height: 160px; transform: rotate(-9deg); }
  .snapshot--hoops .snapshot__photo { height: 131px; background: linear-gradient(#4d84cf, var(--hoops)); }
  .snapshot--soccer { z-index: 2; left: 608px; top: 244px; width: 134px; height: 130px; transform: rotate(1deg); }
  .snapshot--soccer .snapshot__photo { height: 101px; background: linear-gradient(#6d8f6a, var(--soccer)); }

  /* upper row */
  .snapshot--baseball { z-index: 3; left: 494px; top: 74px; width: 108px; height: 150px; transform: rotate(-4deg); }
  .snapshot--baseball .snapshot__photo { height: 121px; background: var(--baseball); }
  .snapshot--tball { z-index: 4; left: 588px; top: 72px; width: 114px; height: 152px; transform: rotate(2deg); }
  .snapshot--tball .snapshot__photo { height: 123px; background: linear-gradient(var(--tball), #a89572); }
  .snapshot--flag { z-index: 5; left: 694px; top: 80px; width: 128px; height: 152px; transform: rotate(9deg); }
  .snapshot--flag .snapshot__photo { height: 123px; background: linear-gradient(#9a9a9a, var(--flag)); }

  .cover-brand {
    position: absolute; right: 16px; top: 404px;
    display: flex; align-items: center; gap: 8px;
    color: var(--white); font-size: 19px; font-weight: 400;
  }
  .cover-brand__dot { width: 14px; height: 14px; border-radius: 50%; background: var(--white); }

  .profile {
    position: absolute; left: 27px; top: 274px;
    width: 238px; height: 238px; box-sizing: border-box;
    background: var(--white); border: 1px solid #c9ccd2; padding: 5px;
    box-shadow: 0 1px 2px rgba(0,0,0,.15);
  }
  .profile__inner {
    width: 100%; height: 100%; background: var(--profile-navy);
    display: flex; flex-direction: column; align-items: center; justify-content: center;
    color: var(--white);
  }
  .profile__dot { width: 22px; height: 22px; border-radius: 50%; background: var(--white); margin: 18px 0 26px; }
  .profile__name { font-size: 19px; font-weight: 400; }

  .actions { position: absolute; top: 467px; left: 821px; display: flex; gap: 16px; }
  .actions__group { display: flex; }
  .actions__btn {
    height: 34px; box-sizing: border-box; padding: 0 12px;
    border: 1px solid var(--btn-border); border-radius: 2px;
    background: var(--btn-bg); color: var(--btn-text);
    font-family: "Open Sans", Arial, sans-serif; font-weight: 700; font-size: 16px;
    display: flex; align-items: center;
  }
  .actions__btn--menu { width: 61px; justify-content: center; gap: 6px; border-left: none; }
</style>
</head>
<body>
<div class="page">
  <section class="cover">
    <div class="splash" role="img" aria-label="Soft paint splash behind the sport snapshots"></div>

    <div class="intro">
      <h1 class="intro__headline">So, what do<br>we offer? It’s right...</h1>
      <p class="intro__ages">Interested? Ages 2 -14</p>
      <a class="intro__signup" href="#signup">Sign up</a>
    </div>

    <svg class="pointers" viewBox="0 0 851 315" aria-hidden="true">
      <defs>
        <marker id="tip" viewBox="0 0 10 10" refX="8" refY="5" markerWidth="7" markerHeight="7" orient="auto-start-reverse">
          <path d="M1 1 L9 5 L1 9" fill="none" stroke="#fff" stroke-width="1.6"/>
        </marker>
      </defs>
      <text class="pointers__label" x="270" y="49">here</text>
      <path class="pointers__arrow" marker-end="url(#tip)" d="M288 62 Q284 102 338 110"/>
      <text class="pointers__label" x="547" y="50">here</text>
      <path class="pointers__arrow" marker-end="url(#tip)" d="M582 22 Q548 8 516 34"/>
      <text class="pointers__label" x="644" y="46">here</text>
      <path class="pointers__arrow" marker-end="url(#tip)" d="M661 60 Q668 100 618 106"/>
      <text class="pointers__label" x="236" y="199">here</text>
      <path class="pointers__arrow" marker-end="url(#tip)" d="M262 212 Q268 242 322 240"/>
      <text class="pointers__label" x="690" y="193">here</text>
      <path class="pointers__arrow" marker-end="url(#tip)" d="M684 168 Q660 148 638 172"/>
      <text class="pointers__label" x="582" y="284">here</text>
      <path class="pointers__arrow" marker-end="url(#tip)" d="M566 288 Q520 296 506 264"/>
    </svg>

    <figure class="snapshot snapshot--volley">
      <div class="snapshot__photo" role="img" aria-label="Photo of volleyball players at the net at sunset"></div>
      <figcaption class="snapshot__caption">– Volleyball •</figcaption>
    </figure>
    <figure class="snapshot snapshot--hoops">
      <div class="snapshot__photo" role="img" aria-label="Photo of a basketball hoop and net"></div>
      <figcaption class="snapshot__caption">• Basketball •</figcaption>
    </figure>
    <figure class="snapshot snapshot--soccer">
      <div class="snapshot__photo" role="img" aria-label="Photo of a soccer ball on grass"></div>
      <figcaption class="snapshot__caption">• Soccer •</figcaption>
    </figure>
    <figure class="snapshot snapshot--baseball">
      <div class="snapshot__photo" role="img" aria-label="Photo of a baseball resting in a glove"></div>
      <figcaption class="snapshot__caption">• Baseball •</figcaption>
    </figure>
    <figure class="snapshot snapshot--tball">
      <div class="snapshot__photo" role="img" aria-label="Photo of a young T-Ball player running on a field"></div>
      <figcaption class="snapshot__caption">• T-Ball •</figcaption>
    </figure>
    <figure class="snapshot snapshot--flag">
      <div class="snapshot__photo" role="img" aria-label="Photo of a football with a flag belt"></div>
      <figcaption class="snapshot__caption">• Flag Football •</figcaption>
    </figure>

    <div class="cover-brand">
      <span class="cover-brand__dot"></span>
      <span class="cover-brand__name">PebblePeak Sprinters</span>
    </div>
  </section>

  <div class="profile">
    <div class="profile__inner">
      <span class="profile__dot"></span>
      <span class="profile__name">PebblePeak Sprinters</span>
    </div>
  </div>

  <div class="actions">
    <span class="actions__btn">Update Info</span>
    <div class="actions__group">
      <span class="actions__btn">Activity Log</span>
      <span class="actions__btn actions__btn--menu">
        <svg width="14" height="14" viewBox="0 0 14 14" aria-hidden="true">
          <circle cx="7" cy="7" r="4" fill="none" stroke="#333" stroke-width="2.4" stroke-dasharray="2 1.4"/>
          <circle cx="7" cy="7" r="1.4" fill="#333"/>
        </svg>
        <svg width="10" height="6" viewBox="0 0 10 6" aria-hidden="true"><path d="M0 0 H10 L5 6 Z" fill="#4d6fb6"/></svg>
      </span>
    </div>
  </div>
</div>
</body>
</html>
```